Beveradge Can Body Print Design - Serious Style

We need a package design for new company Australia.Our products are Canned Drinking Water. We manufacture revolutionary healthy hydrogen water. It is beneficial to human health. The water is filled in standard 250ml Aluminum Beverage cans, Can is 125mm high, diameter is 53mm. if we unfold the can into flat surface, its printable area is 164mm long x 125mm high. All the design will be fitted into this area with bleeding. We also need a logo (to be designed separately) and Wording "Hydroge Water" on the print. We hope to use an abstract design (ideally with 1 or a few simple lines) to reflex a drop or drops of water or current / waves of water in a simple pattern in mono or at most 2 colors. Example of the preferred logo can be found in the attachments. together with some real samples of similar water cans. The successful designers will be invited to the carton box package and other series of our product packages designs. (In the attachment, with a2.jpg, please refer the can design only. the other packages design will be launched in separate projects)
Target Market(s)
all people who drink canned water. in particular, those who pay more attention to healthy lifestyle
Industry/Entity Type
Health Product
Logo Text
something suggesting natural or healthy lifestyle. Or any shape resembles the Letter "H"
Requirements
Must have
- something related to drops or ponds of water, or water wave, or anything reminds water
Nice to have
- This product has substantial benefits to human health. and the methods to make this type of water are purely mechanical, natural, no any harmful chemicals involved. It is also environmental friendly. It is new, not many people recognize it for now. but it will surely go into peoples' daily lives for its substantial natural way of maintaining peoples' healthy-being

```html
<!DOCTYPE html>
<html lang="en">
<head>
<meta charset="utf-8">
<title>Aquelle Hydrogen Water – Can Print</title>
<link href="https://fonts.googleapis.com/css2?family=Montserrat:wght@600;700&family=Mukta:wght@300&display=swap" rel="stylesheet">
<style>
  :root {
    --backdrop-light: #ffffff;
    --backdrop-grey: #dcdcdc;
    --label-white: #ffffff;
    --deep-navy: #2a2f63;
    --brand-navy: #2b2f5e;
    --aqua: #3cb4e5;
    --aqua-soft: #8fd3f0;
  }
  html, body {
    margin: 0;
    padding: 0;
    width: 1200px;
    height: 1032px;
    overflow: hidden;
  }
  body {
    background: radial-gradient(ellipse at 50% 45%, var(--backdrop-light) 35%, var(--backdrop-grey) 100%);
  }
  .can-print {
    display: block;
    width: 1200px;
    height: 1032px;
  }
  .label-base { fill: var(--label-white); }
  .navy-wave { fill: var(--deep-navy); }
  .wave-line-main { fill: none; stroke: var(--aqua); stroke-width: 6; }
  .wave-line-soft { fill: none; stroke: var(--aqua-soft); stroke-width: 2; }
  .brand-dot { fill: var(--aqua); }
  .brand-name {
    font-family: "Montserrat", sans-serif;
    font-weight: 600;
    font-size: 50px;
    fill: var(--brand-navy);
  }
  .brand-tagline {
    font-family: "Montserrat", sans-serif;
    font-weight: 600;
    font-size: 18px;
    letter-spacing: 3px;
    fill: var(--aqua);
  }
  .product-line {
    font-family: "Mukta", sans-serif;
    font-weight: 300;
    font-size: 38px;
    fill: var(--label-white);
  }
  .claim {
    font-family: "Montserrat", sans-serif;
    font-weight: 700;
    font-size: 14px;
    fill: var(--label-white);
  }
  .volume {
    font-family: "Montserrat", sans-serif;
    font-weight: 700;
    font-size: 12px;
    fill: var(--label-white);
  }
</style>
</head>
<body>
<svg class="can-print" viewBox="0 0 1200 1032" xmlns="http://www.w3.org/2000/svg" aria-label="Aquelle hydrogen water can print">
  <defs>
    <clipPath id="label-area">
      <rect x="418" y="155" width="370" height="705" rx="6"/>
    </clipPath>
  </defs>

  <g class="print-area" clip-path="url(#label-area)">
    <rect class="label-base" x="418" y="155" width="370" height="705"/>
    <g transform="translate(418 155)">
      <path class="navy-wave" d="M0,0 H87 C50,90 20,200 60,290 C100,370 250,380 370,465 V705 H0 Z"/>
      <path class="wave-line-main" d="M99,-5 C62,90 34,200 72,285 C112,362 255,372 375,455"/>
      <path class="wave-line-soft" d="M110,-5 C74,90 46,198 84,280 C124,354 262,364 375,446"/>
    </g>
  </g>

  <g class="brand-block">
    <circle class="brand-dot" cx="612" cy="285" r="20"/>
    <text class="brand-name" x="612" y="387" text-anchor="middle" textLength="234" lengthAdjust="spacingAndGlyphs">AQUELLE</text>
    <text class="brand-tagline" x="612" y="420" text-anchor="middle">HYDROGEN WATER</text>
  </g>

  <g class="product-copy">
    <text class="product-line" x="612" y="674" text-anchor="middle">hydrogen enriched</text>
    <text class="product-line" x="612" y="716" text-anchor="middle">drinking water</text>
    <text class="claim" x="612" y="760" text-anchor="middle">NO ANY HARMFUL</text>
    <text class="claim" x="612" y="779" text-anchor="middle">CHEMICALS INVOLVED</text>
    <text class="volume" x="612" y="840" text-anchor="middle">250ML</text>
  </g>
</svg>
</body>
</html>
```